Booklet - I can pay more Urgent Project

Dear,
I need help to design a booklet for my startup, I have provided a booklet sample I want the same layout and organization. As you can see I'm not looking for a lot of colors or graphs, it should clean neat. The booklet size could be 8.5 x 11 or 8.5x5.5. This is urgent I need it in 24hr max.
My booklet content on word file named "Moss Lantern Booklet".
Booklet sample is on pdf file named "bookt_sample".
Nice cover design is helpful
Thank you.

Requirements
Must have
• Need to go to print by tomorrow - urgent project

```html
<!DOCTYPE html>
<html lang="en">
<head>
<meta charset="utf-8">
<title>Moss Lantern – User Guide</title>
<link href="https://fonts.googleapis.com/css2?family=Jost:ital,wght@0,300;0,400;0,600;1,300&family=Arimo:wght@400;700&display=swap" rel="stylesheet">
<style>
:root{
  --accent:#23a9e1;
  --ink:#2b2b2b;
  --band:#545454;
  --screen-bg:#f5f5f5;
  --screen-line:#d6d6e4;
  --field:#fbf6c4;
  --navy:#2d3580;
  --link:#3668b8;
}
*{margin:0;padding:0;box-sizing:border-box}
html,body{width:777px;height:1200px;overflow:hidden;background:#fff}
body{position:relative;font-family:"Jost",sans-serif;font-weight:300;color:var(--ink)}
.abs{position:absolute}
.tab{left:70px;top:0}
.title{left:70px;top:116px;font-size:46px;font-weight:300;letter-spacing:.5px}
.steps{left:70px;top:216px;font-size:17.5px;line-height:23px;list-style:none}
.steps li span{display:inline-block;width:26px}
.badge{left:48px;top:289px;width:45px;height:45px;border-radius:50%;background:var(--accent);color:#fff;font-weight:600;font-size:24px;display:flex;align-items:center;justify-content:center;z-index:2}
.screen{background:var(--screen-bg);box-shadow:0 2px 8px rgba(0,0,0,.35);overflow:hidden;font-family:"Arimo",sans-serif}
.screen-head{height:24px;background:#fff;border-bottom:1px solid var(--screen-line);position:relative;font-size:7.5px;color:#333}
.brand{position:absolute;left:40px;top:8px;color:#333}
.nav{position:absolute;top:5px;font-size:5.5px;display:flex;gap:6px;align-items:center}
.nav span{padding:2px 6px;border-radius:7px;color:var(--navy)}
.nav .on{background:var(--navy);color:#fff}
.screen-foot{position:absolute;left:0;right:0;bottom:0;height:24px;background:var(--band);color:#bbb;font-size:3px;padding:9px 0 0 48px}
.login-box{position:absolute;left:146px;top:44px;width:125px;height:98px;background:#fff;border:1px solid #ccc;box-shadow:0 1px 2px rgba(0,0,0,.15);padding:0 22px;font-size:5.5px}
.login-box h3{text-align:center;font-size:9.5px;font-weight:400;margin:2px 0 5px}
.login-box label{display:block;font-weight:700}
.login-box .field{height:10px;background:var(--field);border-bottom:1px solid #ccc;margin:1px 0 13px;padding:2px 1px;font-size:5.5px}
.login-box .submit{display:block;margin:-4px auto 0;width:24px;border:1px solid #aaa;background:#eee;text-align:center;font-size:5px;padding:1px 0;font-weight:700}
.caption{font-style:italic;font-size:11px;color:#444}
.body-text{font-size:17.5px;line-height:22.5px;color:var(--ink)}
.bullets{list-style:none;margin-top:9px}
.bullets li{position:relative;padding-left:35px;margin-bottom:9px}
.bullets li::before{content:"·";position:absolute;left:17px;font-weight:600}
.artists-panel{position:absolute;left:35px;top:42px;width:305px;height:158px;background:#fff;border:1px solid #ccc;box-shadow:1px 1px 2px rgba(0,0,0,.2);font-size:8px}
.artists-panel h3{position:absolute;left:138px;top:6px;font-size:8.5px;font-weight:400}
.artist{position:absolute;top:23px;width:60px;text-align:center;color:var(--link);font-size:7px}
.avatar{width:59px;height:59px;border:1px solid #ccc;margin-bottom:12px}
.footer{left:0;top:1147px;width:777px;height:53px;background:var(--band);color:#fff;font-family:"Jost",sans-serif;font-weight:600;font-size:14.5px}
.footer .page{position:absolute;left:35px;top:17px}
.footer .site{position:absolute;right:35px;top:17px}
</style>
</head>
<body>
<svg class="abs tab" width="100" height="113" viewBox="0 0 100 113"><polygon points="0,0 100,0 100,82 0,113" fill="var(--accent)"/></svg>
<h1 class="abs title">User Guide</h1>
<ol class="abs steps">
  <li><span>1.</span>Type https://mosslantern.net/login.php in browser for login</li>
  <li><span>2.</span>Type https://mosslantern.net to go to the main page</li>
</ol>

<div class="abs badge">1</div>
<div class="abs screen" style="left:70px;top:310px;width:424px;height:242px">
  <div class="screen-head">
    <div class="brand">Moss Lantern Where Story Matters</div>
    <div class="nav" style="left:308px"><span>Artists</span><span class="on">Login</span></div>
  </div>
  <div class="login-box">
    <h3>LOGIN</h3>
    <label>Username</label><div class="field">quillmere@mail.test</div>
    <label>Password</label><div class="field">•••••••••••</div>
    <span class="submit">Submit</span>
  </div>
  <div class="screen-foot">Copyright 2024 · All rights reserved · Moss Lantern Studio</div>
</div>
<p class="abs caption" style="left:70px;top:559px">Figure 3 - Login Page</p>

<div class="abs body-text" style="left:512px;top:306px;width:185px">
  Two options are available at the login page:
  <ul class="bullets">
    <li>Artists</li>
    <li>Login: Enter the username and the password and press “Submit” button</li>
  </ul>
</div>

<p class="abs body-text" style="left:70px;top:739px;width:200px">Artists page will show all the artists of the site, by clicking on the avatars, the user can view their gallery.</p>

<div class="abs screen" style="left:282px;top:744px;width:424px;height:236px">
  <div class="screen-head">
    <div class="brand">Moss Lantern Where Story Matters</div>
    <div class="nav" style="left:278px"><span class="on">Artists</span><span>Login</span></div>
  </div>
  <div class="artists-panel">
    <h3>Artists</h3>
    <div class="artist" style="left:7px">
      <div class="avatar" role="img" aria-label="Artist avatar illustration" style="background:linear-gradient(135deg,#b98a4a,#7d5a30)"></div>Quillmere
    </div>
    <div class="artist" style="left:70px">
      <div class="avatar" role="img" aria-label="Artist avatar illustration" style="background:linear-gradient(180deg,#f3d84a,#e9e6d8)"></div>Tavi
    </div>
  </div>
  <div class="screen-foot">Copyright 2024 · All rights reserved · Moss Lantern Studio</div>
</div>
<p class="abs caption" style="left:282px;top:989px">Figure 4 - Main Page (Before Login)</p>

<footer class="abs footer"><span class="page">13</span><span class="site">MossLantern.net</span></footer>
</body>
</html>
```